Business Card Design/Logo

I require a design/logo for my own Company, Morvane. The Jewellery I make is totally hand crafted. I own a hand Mining Claim out in the gemfields of Queensland and dig up my own stones. I also fossick for Gold Locally so all my Jewellery products are hand dug/cut/created. Quality stones are hand cut by my partner (Faceted) and other stones (Seconds) are either skin polished or recessed into pieces of Solid 925 Silver or Solid 9ct and 18 ct Gold. I make Sets (Collections) or just one-of designs. All the stones come in different colours and I am now starting to use different colour Golds. The final design should radiate professionalism, quality and uniqueness.

Target Market(s)

Many designs will cost a minimum of AU Dollars $2,000

Industry/Entity Type

Business

Contact Information for Business Card

Morvane Creations
Unique Hand Made Australian Jewellery
0400839627
P.O. Box 517 Tallowgrove 4718 Qld
morvanegems@quillpost.example

```html
<!DOCTYPE html>
<html lang="en">
<head>
<meta charset="utf-8">
<title>Morvane Creations — Business Card</title>
<link rel="stylesheet" href="https://fonts.googleapis.com/css2?family=Questrial&family=Montserrat:wght@600&display=swap">
<style>
  :root {
    --backdrop: #e4e2dd;
    --card-dark: #2d2d2d;
    --card-light: #f7f7f6;
    --stripe-dark: rgba(255,255,255,0.13);
    --stripe-faint: rgba(255,255,255,0.07);
    --stripe-light: rgba(0,0,0,0.035);
    --ink-light: #ffffff;
    --ink-dark: #3a3a3a;
    --ink-muted: #5a5a5a;
  }
  * { margin: 0; padding: 0; box-sizing: border-box; }
  html, body { width: 1200px; height: 911px; overflow: hidden; }
  body {
    background: var(--backdrop);
    position: relative;
    font-family: "Questrial", sans-serif;
  }
  .card {
    position: absolute;
    left: 240px;
    width: 720px;
    height: 411px;
    overflow: hidden;
    box-shadow: 0 6px 18px rgba(0,0,0,0.18);
  }
  .card--back { top: 24px; background: var(--card-dark); }
  .card--front { top: 476px; background: var(--card-light); }
  .stripes { position: absolute; inset: 0; width: 100%; height: 100%; }

  .brand { position: absolute; }
  .brand__name {
    font-family: "Questrial", sans-serif;
    font-size: 38px;
    letter-spacing: 3px;
    line-height: 1;
  }
  .brand__tagline {
    font-family: "Questrial", sans-serif;
    font-size: 13px;
    letter-spacing: 0.4px;
    margin-top: 8px;
  }
  .card--back .brand { left: 52px; top: 154px; color: var(--ink-light); }

  .card--front .brand { right: 60px; top: 44px; color: var(--ink-dark); text-align: left; }
  .card--front .brand__name { font-size: 31px; }
  .card--front .brand__tagline { font-size: 11.5px; color: var(--ink-muted); }

  .person { position: absolute; left: 46px; top: 52px; }
  .person__name {
    font-family: "Montserrat", sans-serif;
    font-weight: 600;
    font-size: 17px;
    letter-spacing: 0.8px;
    color: var(--ink-dark);
  }
  .person__role { font-size: 14px; color: var(--ink-muted); margin-top: 2px; }

  .contact { position: absolute; left: 72px; bottom: 38px; list-style: none; }
  .contact__item {
    display: flex; align-items: center; gap: 10px;
    font-size: 14px; letter-spacing: 0.6px;
    color: var(--ink-muted); line-height: 20px;
  }
  .contact__icon { width: 12px; height: 12px; fill: var(--ink-muted); flex: none; }
</style>
</head>
<body>

<section class="card card--back" aria-label="Card back">
  <svg class="stripes" viewBox="0 0 720 411" aria-hidden="true">
    <polygon points="590,0 612,0 352,411 330,411" fill="var(--stripe-dark)"/>
    <polygon points="628,0 646,0 386,411 368,411" fill="var(--stripe-dark)"/>
    <polygon points="670,0 720,0 720,40 460,411 410,411" fill="var(--stripe-faint)"/>
  </svg>
  <div class="brand">
    <div class="brand__name">MORVANE</div>
    <div class="brand__tagline">Hand Made Australian Jewellery</div>
  </div>
</section>

<section class="card card--front" aria-label="Card front">
  <svg class="stripes" viewBox="0 0 720 411" aria-hidden="true">
    <polygon points="620,0 642,0 382,411 360,411" fill="var(--stripe-light)"/>
    <polygon points="660,0 676,0 416,411 400,411" fill="var(--stripe-light)"/>
  </svg>

  <div class="person">
    <div class="person__name">DALE HARGREAVE</div>
    <div class="person__role">Founder &amp; CEO</div>
  </div>

  <div class="brand">
    <div class="brand__name">MORVANE</div>
    <div class="brand__tagline">Hand Made Australian Jewellery</div>
  </div>

  <ul class="contact">
    <li class="contact__item">
      <svg class="contact__icon" viewBox="0 0 12 12" aria-hidden="true"><rect x="1" y="0" width="10" height="12" rx="1.5"/><rect x="3" y="2" width="6" height="6" fill="var(--card-light)"/></svg>
      +631.555.0172
    </li>
    <li class="contact__item">
      <svg class="contact__icon" viewBox="0 0 12 12" aria-hidden="true"><rect x="0" y="2" width="12" height="8"/><polyline points="0.5,2.5 6,7 11.5,2.5" fill="none" stroke="var(--card-light)" stroke-width="1.2"/></svg>
      morvanegems@quillpost.example
    </li>
    <li class="contact__item">
      <svg class="contact__icon" viewBox="0 0 12 12" aria-hidden="true"><path d="M6 0a4.2 4.2 0 0 0-4.2 4.2C1.8 7.4 6 12 6 12s4.2-4.6 4.2-7.8A4.2 4.2 0 0 0 6 0z"/><circle cx="6" cy="4.3" r="1.6" fill="var(--card-light)"/></svg>
      P.O. Box 517 Tallowgrove, 4718 Qld
    </li>
  </ul>
</section>

</body>
</html>
```